Book for new dads needs a cover.

We need a cover for a book titled Roadmap for Brand-New Fathers: Practical Lessons for Getting Through the Nine Months, Juggling Career and Home, and Keeping a Steady Mind on the Way to Parenthood. We would like to see a design that emphasizes healthy babies and confident dads.

```html
<!DOCTYPE html>
<html lang="en">
<head>
<meta charset="utf-8">
<title>Roadmap for Brand-New Fathers — Book Cover</title>
<link rel="stylesheet" href="https://fonts.googleapis.com/css2?family=Barlow+Condensed:wght@400;600;700&display=swap">
<style>
  :root {
    --backdrop: #262626;
    --sky-top: #25507a;
    --sky-mid: #6f7f8c;
    --haze: #c4a181;
    --glow: #ec8a4c;
    --ember: #ef5a27;
    --shore: #3e2626;
    --accent-yellow: #ffb806;
    --title-white: #ffffff;
  }
  * { margin: 0; padding: 0; box-sizing: border-box; }
  html, body {
    width: 1200px;
    height: 1200px;
    overflow: hidden;
    background: var(--backdrop);
  }
  .book-cover {
    position: absolute;
    left: 217px;
    top: 26px;
    width: 765px;
    height: 1148px;
    overflow: hidden;
  }
  .cover-photo {
    position: absolute;
    inset: 0;
    background: linear-gradient(180deg,
      var(--sky-top) 0%,
      #3a6180 18%,
      var(--sky-mid) 38%,
      var(--haze) 52%,
      var(--glow) 68%,
      var(--ember) 84%,
      #8a3a2a 93%,
      var(--shore) 100%);
  }
  .cover-type {
    position: absolute;
    inset: 0;
    width: 765px;
    height: 1148px;
    font-family: "Barlow Condensed", "Arial Narrow", sans-serif;
  }
  .subtitle-lead { fill: var(--accent-yellow); font-weight: 700; font-size: 42px; }
  .subtitle-body { fill: var(--title-white); font-weight: 400; font-size: 31px; }
  .title-key { fill: var(--accent-yellow); font-weight: 600; font-size: 255px; }
  .title-line { fill: var(--title-white); font-weight: 600; font-size: 143px; }
  .title-hero { fill: var(--title-white); font-weight: 600; font-size: 400px; }
  .author-name { fill: var(--title-white); font-weight: 600; font-size: 106px; }
</style>
</head>
<body>
  <div class="book-cover">
    <div class="cover-photo" role="img" aria-label="Photograph of a father silhouetted against a sunset sky at the seashore, carrying his young child on his shoulders, both with arms spread wide"></div>
    <svg class="cover-type" viewBox="0 0 765 1148" aria-label="Cover text">
      <text class="subtitle-lead" x="58" y="85" textLength="648" lengthAdjust="spacingAndGlyphs">PRACTICAL LESSONS FOR GETTING THROUGH</text>
      <text class="subtitle-body" x="41" y="120" textLength="682" lengthAdjust="spacingAndGlyphs">THE NINE MONTHS, JUGGLING CAREER AND HOME, AND KEEPING</text>
      <text class="subtitle-body" x="70" y="155" textLength="624" lengthAdjust="spacingAndGlyphs">A STEADY MIND ON THE WAY TO PARENTHOOD.</text>

      <text class="title-key" x="69" y="372" textLength="631" lengthAdjust="spacingAndGlyphs">ROADMAP</text>
      <text class="title-line" x="50" y="489" textLength="671" lengthAdjust="spacingAndGlyphs">FOR BRAND-NEW</text>
      <text class="title-hero" x="73" y="788" textLength="623" lengthAdjust="spacingAndGlyphs">FATHERS</text>

      <text class="author-name" x="69" y="1098" textLength="633" lengthAdjust="spacing">AUTHOR NAME</text>
    </svg>
  </div>
</body>
</html>
```